Tarnwick Nectar needs a great booklet

We need a booklet design for our Raw Honey business that is based in Dubai. Something clean and niche as our honey is special /very expensive. We have 12 types of honey and each type has its health benefits. As well we are very active on social media so will be good to be very creative and find a way through out this booklet to connect with the consumer. DO NOT inspire from the material i have send you (with the exception of wording)as this was done at the beginning of our business year so we would like something different.
I have attached the specs as we will be printing it in that format. We are looking to find a design source for future projects in various media formats.
Try to use a clean font and not funny ones (please try and find TARNWICK'S LOGO fonts)
For knowing more of who we are please have a look at our instagram account: tarnwicknectarae
THE FINAL DESIGN SHOULD LOOK LIKE A EDUCATIONAL BOOK FOR HONEY USERS BUT HAVE A PERSONAL FEEL. BE CREATIVE! HAVE FUN!
Updates

Please don't post anything that is similar to the options i got so far as it is a no for that kind. Added Wednesday, April 12, 2017

Industry/Entity Type

Business

Colors

Designer to choose colors to be used in the design.

Requirements
Must have
• a new look and please don't use the artwork/colors of the material i had send as that is to be used only for wording .
• File 1 - has the requirements for number of pages and size of booklet
Nice to have
• new and cool ideas
Should not have
• DO NOT inspire from the material i have send you (with the exception of wording)as this was done at the beginning of our business year so we would like something different.

```html
<!DOCTYPE html>
<html lang="en">
<head>
<meta charset="utf-8">
<title>Tarnwick Nectar Booklet – Spreads</title>
<link href="https://fonts.googleapis.com/css2?family=Arsenal:ital,wght@0,400;1,400&family=Open+Sans:ital,wght@0,300;1,300&display=swap" rel="stylesheet">
<style>
  :root{
    --stage-light:#e4e4e4;
    --stage-dark:#a9a9a9;
    --paper:#ffffff;
    --heading:#7d6244;
    --quote:#7d6244;
    --body:#b09477;
    --body-soft:#d1b59b;
    --band:#f3e4d1;
    --band-strong:#eed7bb;
    --hex-pale:#fbefe8;
    --hex-photo-b:#c9b6a0;
    --divider:#eee4dc;
    --label:#111111;
    --fold:#1a1a1a;
  }
  *{margin:0;padding:0;box-sizing:border-box}
  html,body{width:1200px;height:1200px;overflow:hidden}
  body{
    position:relative;
    background:radial-gradient(ellipse at 50% 50%,var(--stage-light) 0%,#cfcfcf 55%,var(--stage-dark) 100%);
    font-family:"Open Sans",Arial,sans-serif;
  }
  .spread{
    position:absolute;left:234px;width:734px;height:504px;
    background:var(--paper);
    box-shadow:2px 3px 6px rgba(0,0,0,.35);
    overflow:hidden;
  }
  .spread--one{top:62px}
  .spread--two{top:630px}
  .spread-label{
    position:absolute;left:234px;font-family:Arial,Helvetica,sans-serif;
    font-size:25px;color:var(--label);
  }
  .spread-label--one{top:582px}
  .spread-label--two{top:1148px}
  .fold-line{
    position:absolute;left:599px;top:38px;width:2px;height:1120px;
    background:repeating-linear-gradient(to bottom,var(--fold) 0 8px,transparent 8px 16px);
    z-index:5;
  }
  .edge-band{position:absolute;height:22px}
  .edge-band--top{
    left:0;top:22px;width:734px;
    background:linear-gradient(to right,rgba(243,228,209,0) 0%,var(--band) 12%,var(--band-strong) 55%,var(--band) 90%,rgba(243,228,209,.4) 100%);
    opacity:.75;
  }
  .edge-band--bottom{
    left:290px;top:462px;width:444px;
    background:linear-gradient(to right,rgba(243,228,209,0) 0%,var(--band) 25%,var(--band-strong) 100%);
    opacity:.75;
  }
  .site-url{
    position:absolute;left:536px;top:27px;font-size:11px;letter-spacing:.4px;
    color:var(--body);background:var(--paper);padding:0 4px;
  }
  .page-number{position:absolute;left:36px;top:468px;font-size:10px;color:var(--body)}
  .feature-title{
    position:absolute;left:36px;top:84px;
    font-family:"Arsenal",Georgia,serif;font-size:41px;line-height:37px;
    letter-spacing:3px;color:var(--heading);font-weight:400;
  }
  .copy{
    position:absolute;width:290px;font-size:11px;line-height:13.7px;
    color:var(--body);font-weight:300;
  }
  .copy p+p{margin-top:10.5px}
  .copy--left{left:36px;top:224px}
  .copy--right{left:402px;top:224px}
  .hex-row{position:absolute;left:388px;top:61px}
  .product{position:absolute;width:296px}
  .product h2{
    font-family:"Arsenal",Georgia,serif;font-weight:400;font-size:20px;
    line-height:23px;color:var(--heading);
  }
  .product .tagline{
    font-family:"Arsenal",Georgia,serif;font-style:italic;font-size:13.5px;
    line-height:15px;color:var(--quote);margin-top:3px;
  }
  .product .tagline--sans{font-family:"Open Sans",Arial,sans-serif;font-size:10.8px;line-height:14px}
  .product .details{
    font-size:10.9px;line-height:13.8px;color:var(--body-soft);
    font-weight:300;margin-top:10px;
  }
  .divider-dots{position:absolute;display:flex;gap:3px}
  .divider-dots span{width:9px;height:9px;border-radius:50%;background:var(--divider)}
</style>
</head>
<body>

<div class="fold-line"></div>

<section class="spread spread--one">
  <div class="edge-band edge-band--top" role="img" aria-label="Decorative honey-toned band"></div>
  <span class="site-url">WWW.TARNWICKNECTAR.CO</span>

  <h1 class="feature-title">Why<br>the name<br>‘tarnwick’?</h1>

  <div class="copy copy--left">
    <p>Tarnwick is simply a word that describes all the things that exceptional Raw Yemeni Honey brings us. The honey symbolized life, love, joy, fertility, spiritual awakening and good fortune!</p>
    <p>But, even more directly, the name of our brand came from a very special place. I found that even with all of the successes that the world can bring; through blessings, hard work and amazing luck; that it could never really fill your life with enough to make you whole and happy.</p>
    <p>Then I found my life partner, he reminded me how the love and passion of life can lead you to a better place than all of the successes in the world ever could. He calls me “Tarnwick” to symbolize how I seemed to grow and</p>
  </div>

  <svg class="hex-row" width="346" height="112" viewBox="0 0 346 112">
    <defs>
      <linearGradient id="honeycomb" x1="0" y1="0" x2="1" y2="1">
        <stop offset="0" stop-color="#6f5a45"/><stop offset="1" stop-color="#b09a82"/>
      </linearGradient>
      <linearGradient id="jars" x1="0" y1="0" x2="0" y2="1">
        <stop offset="0" stop-color="#5e4c3b"/><stop offset="1" stop-color="#c5b19b"/>
      </linearGradient>
    </defs>
    <polygon points="48,0 96,28 96,84 48,112 0,84 0,28" fill="var(--hex-pale)"/>
    <polygon role="img" aria-label="Sepia photograph of honeycomb" points="155,0 204,28 204,84 155,112 106,84 106,28" fill="url(#honeycomb)"/>
    <polygon role="img" aria-label="Sepia photograph of honey jars on a wooden board" points="261,0 310,28 310,84 261,112 212,84 212,28" fill="url(#jars)"/>
    <polygon role="img" aria-label="Sepia photograph of honey product detail" points="367,0 416,28 416,84 367,112 318,84 318,28" fill="var(--hex-photo-b)"/>
  </svg>

  <div class="copy copy--right">
    <p>become healthier and more vibrant every day that I was freed to enjoy the real meaning of life.</p>
    <p>We look forward to you joining us on our journey, through our exceptional Yemeni Raw Honey<br>and the Tarnwick Nectar brand!</p>
    <p>Lidia Marena Costache<br>Partner &amp; Managing Director</p>
  </div>

  <span class="page-number">5</span>
  <div class="edge-band edge-band--bottom" role="img" aria-label="Decorative honey-toned band"></div>
</section>
<div class="spread-label spread-label--one">Page 3-4</div>

<section class="spread spread--two">
  <div class="edge-band edge-band--top" role="img" aria-label="Decorative honey-toned band"></div>
  <span class="site-url">WWW.TARNWICKNECTAR.CO</span>

  <article class="product" style="left:36px;top:86px">
    <h2>Organic White Honey</h2>
    <p class="tagline">“Purest flavor packed white honey of Kyrgyzstan’s isolated mountains.”</p>
    <p class="details">Honey from the mountains of Kyrgyzstan with a very unique color and texture that has and amazing explosive taste of flowers. Enhances, stimulate and boost the memory taken in combination with walnuts and or dates.</p>
  </article>
  <div class="divider-dots" style="left:153px;top:226px"><span></span><span></span><span></span><span></span><span></span></div>

  <article class="product" style="left:36px;top:251px">
    <h2>Raw Yemeni Honey infused with Blackseed</h2>
    <p class="tagline">“Blackseed and raw honey for health and healing.”</p>
    <p class="details">Tarnwick Blackseed Honey is a treatment for every disease and especially for all types of cancer. The high content of phytosterols in black seed is necessary for our body to produce hormones, vitamin D and bile acid, aiding in healing endocrine disorders, immune deficiencies and cardiovascular diseases.</p>
  </article>

  <article class="product" style="left:402px;top:84px">
    <h2>Raw Yemeni Honey infused with Cinnamon</h2>
    <p class="tagline">“Cinnamon and raw honey for health and healing.”</p>
    <p class="details">Tarnwick Cinnamon Raw Honey blend has been found to be a miraculous recipe that helps to prevent heart disease and regulate blood sugar. It also reduces LDL cholesterol levels, helps in digestion, cures various skin infections and helps to lose weight.</p>
  </article>
  <div class="divider-dots" style="left:519px;top:246px"><span></span><span></span><span></span><span></span><span></span></div>

  <article class="product" style="left:402px;top:284px">
    <h2>Raw Yemeni Honey and Royal Jelly</h2>
    <p class="tagline tagline--sans"><em>“Most luxurious nectar of the ancient Sidr tree in Yemen with Royal Jelly.”</em></p>
    <p class="details">Tarnwick Raw Yemeni Honey and Royal Jelly join to create a miraculous mix for increasing longevity and making every day better! This unique blend treats ulcers, improves cardiovascular health, helps reduce inflammation, balances our immune systems, enhances brain function and offers superior liver protection.</p>
  </article>

  <span class="page-number">9</span>
  <div class="edge-band edge-band--bottom" role="img" aria-label="Decorative honey-toned band"></div>
</section>
<div class="spread-label spread-label--two">Page 5-6</div>

</body>
</html>
```